Service business needs Business Card Design

Looking to create a new business card design that is both professional and unique the can highlight the many services we offer throughout the seasons. Our tagline is "The Steadfast Touch"
Licensed & Insured: PA392617 has to be small and on the back side of the card.
On the Front:
FirstName LastName
Title
We offer the following services:
Deck Repair and Maintenance
Deck Cleaning and Staining/Painting
Power Washing/House Washing
Landscape Lighting Installation
Christmas Lighting Installation

```html
<!DOCTYPE html>
<html lang="en">
<head>
<meta charset="utf-8">
<title>Halden Services – Business Card</title>
<link href="https://fonts.googleapis.com/css2?family=Montserrat:wght@400;500;600&family=Roboto+Condensed:wght@400;500&display=swap" rel="stylesheet">
<style>
  :root {
    --page-bg: #0e0e10;
    --card-bg: #26272b;
    --brand-blue: #0a5aa8;
    --accent-blue: #1ea3e0;
    --band-blue: #064f93;
    --text-light: #f1f3f5;
    --text-soft: #c9ced4;
  }
  * { box-sizing: border-box; margin: 0; padding: 0; }
  html, body { width: 1200px; height: 820px; overflow: hidden; }
  body {
    background: var(--page-bg);
    font-family: "Montserrat", Arial, sans-serif;
    display: flex; align-items: center; justify-content: center; gap: 30px;
  }
  .card {
    position: relative;
    width: 560px; height: 320px;
    background: var(--card-bg);
    overflow: hidden;
    border-left: 4px solid var(--accent-blue);
  }
  /* Front */
  .brand {
    position: absolute; top: 48px; right: 40px;
    display: flex; align-items: center; gap: 12px;
  }
  .brand-dot { width: 22px; height: 22px; border-radius: 50%; background: var(--accent-blue); }
  .brand-name {
    font-weight: 500; font-size: 26px; letter-spacing: 3px;
    color: var(--brand-blue); text-transform: uppercase;
  }
  .rule-long {
    position: absolute; top: 116px; left: 180px; right: 0;
    height: 1px; background: var(--accent-blue);
  }
  .person { position: absolute; top: 126px; left: 38px; }
  .person-name {
    font-weight: 600; font-size: 19px; line-height: 23px; color: var(--brand-blue);
    text-transform: uppercase; letter-spacing: .5px;
  }
  .person-title { font-size: 15px; line-height: 20px; color: var(--text-light); margin-top: 2px; }
  .rule-short { width: 200px; height: 1px; background: var(--accent-blue); margin: 8px 0 9px; }
  .contact-list { list-style: none; }
  .contact-list li {
    display: flex; align-items: center; gap: 8px;
    font-size: 14px; color: var(--text-light); line-height: 20px;
  }
  .contact-list svg { width: 13px; height: 13px; flex: none; fill: none; stroke: var(--brand-blue); stroke-width: 2; }
  .contact-list .hl { color: var(--brand-blue); }
  .license {
    position: absolute; right: 36px; bottom: 68px;
    font-size: 12px; color: var(--text-light);
  }
  .license span { color: var(--accent-blue); }
  .tagline-band {
    position: absolute; left: 0; right: 0; bottom: 0; height: 50px;
    background: var(--band-blue);
    display: flex; align-items: center; justify-content: center;
  }
  .tagline {
    font-weight: 500; font-size: 18px; letter-spacing: 1px;
    color: var(--text-light); text-transform: uppercase;
  }
  /* Back */
  .services { position: absolute; top: 86px; left: 48px; width: 260px; }
  .services-heading {
    font-family: "Roboto Condensed", Arial, sans-serif;
    font-size: 15px; font-weight: 500; color: var(--accent-blue);
    text-transform: uppercase; line-height: 18px; margin-bottom: 8px;
  }
  .services-list { list-style: none; padding-left: 18px; }
  .services-list li {
    font-family: "Roboto Condensed", Arial, sans-serif;
    font-size: 15px; color: var(--text-light); line-height: 21px;
  }
</style>
</head>
<body>

  <section class="card card-front" aria-label="Card front">
    <div class="brand">
      <span class="brand-dot"></span>
      <span class="brand-name">Halden Services</span>
    </div>
    <div class="rule-long"></div>
    <div class="person">
      <p class="person-name">Daniel Carter</p>
      <p class="person-title">Managing Director</p>
      <div class="rule-short"></div>
      <ul class="contact-list">
        <li><svg viewBox="0 0 16 16"><path d="M4 1.5l2.5 3-1.5 1.5a8 8 0 0 0 5 5l1.5-1.5 3 2.5-1.5 2.5C7 14 2 9 1.5 3z"/></svg><span>044-555 018 274</span></li>
        <li><svg viewBox="0 0 16 16"><rect x="1.5" y="3.5" width="13" height="9"/><path d="M1.5 3.5l6.5 5 6.5-5"/></svg><span>info@haldenmail.com</span></li>
        <li><svg viewBox="0 0 16 16"><circle cx="8" cy="8" r="6.5"/><path d="M1.5 8h13M8 1.5c3 3 3 10 0 13M8 1.5c-3 3-3 10 0 13"/></svg><span>www.<span class="hl">haldenhome</span>.com</span></li>
      </ul>
    </div>
    <p class="license"><span>Licensed &amp; Insured</span>: PA392617</p>
    <div class="tagline-band"><p class="tagline">The Steadfast Touch</p></div>
  </section>

  <section class="card card-back" aria-label="Card back">
    <div class="services">
      <p class="services-heading">We offer the following<br>services</p>
      <ul class="services-list">
        <li>Deck Repair and Maintenance</li>
        <li>Deck Cleaning and<br>Staining/Painting</li>
        <li>Power Washing/House Washing</li>
        <li>Landscape Lighting Installation</li>
        <li>Christmas Lighting Installation</li>
      </ul>
    </div>
  </section>

</body>
</html>
```